Four nights by a quiet harbour

Creation of the cover for the book: "Trois saisons au bord du vieux port" with the joined photo of a 70 years old lady.
Title: "Four nights beside the quiet harbour"
Author: "Mireille Cantal"
Publisher: "Editions Basalte" (should be at the bottom of the page)
Format: 14 x 20.5 cm
The story: A senior lady (70 years old), divorced, with a beautiful face, still wants to seduce, even young men.
We found the perfect photo for the woman. We would like to ask you to make a modern cover from it.
Updates
Besoin de quelques jours pour choisir un design
Target Market(s)
Novels reader (adults)
Industry/Entity Type
book
Look and feel
Each slider illustrates characteristics of the customer's brand and the style your logo design should communicate.

```html
<!DOCTYPE html>
<html lang="fr">
<head>
<meta charset="utf-8">
<title>Trois saisons au bord du vieux port — Mireille Cantal</title>
<link href="https://fonts.googleapis.com/css2?family=Allura&family=Cinzel:wght@400&family=Cormorant+Garamond:wght@500&family=Libre+Baskerville&display=swap" rel="stylesheet">
<style>
  :root {
    --cover-green: #4f5b59;
    --cover-green-deep: #485452;
    --hair-light: #d9dcda;
    --hair-mid: #a9b0ad;
    --skin-warm: #c9a89c;
    --ink-white: #ffffff;
    --ink-dark: #1d2120;
  }
  html, body {
    margin: 0;
    padding: 0;
    overflow: hidden;
    background: var(--cover-green);
  }
  .book-wrap {
    position: relative;
    width: 1200px;
    height: 830px;
    overflow: hidden;
    background: linear-gradient(180deg, var(--cover-green) 0%, var(--cover-green-deep) 100%);
    color: var(--ink-white);
  }

  /* Back cover */
  .back-title {
    position: absolute;
    left: 90px;
    top: 90px;
    width: 380px;
    text-align: center;
  }
  .back-title .script {
    display: block;
    font-family: "Allura", cursive;
    font-size: 36px;
    line-height: 40px;
    white-space: nowrap;
  }
  .back-title .script-small {
    display: block;
    font-family: "Allura", cursive;
    font-size: 20px;
    line-height: 18px;
    white-space: nowrap;
  }
  .back-title .caps {
    display: block;
    font-family: "Cinzel", serif;
    font-size: 34px;
    line-height: 38px;
  }
  .blurb {
    position: absolute;
    left: 70px;
    top: 216px;
    width: 418px;
    margin: 0;
    font-family: "Libre Baskerville", serif;
    font-size: 11.6px;
    line-height: 16.8px;
    text-align: justify;
    text-align-last: center;
    hyphens: auto;
  }
  .code-box {
    position: absolute;
    left: 70px;
    top: 698px;
    width: 124px;
    height: 83px;
    background: var(--ink-white);
  }
  .publisher {
    font-family: "Cormorant Garamond", serif;
    font-weight: 500;
    font-size: 20px;
    letter-spacing: 0.02em;
    text-transform: uppercase;
    white-space: nowrap;
  }
  .back-publisher {
    position: absolute;
    left: 214px;
    top: 758px;
  }

  /* Spine */
  .spine {
    position: absolute;
    left: 560px;
    top: 0;
    width: 72px;
    height: 830px;
  }
  .spine-title {
    position: absolute;
    left: 20px;
    top: 28px;
    writing-mode: vertical-rl;
    white-space: nowrap;
    font-family: "Allura", cursive;
    font-size: 30px;
    line-height: 1;
  }
  .spine-title .caps {
    font-family: "Cinzel", serif;
    font-size: 19px;
  }
  .spine-author {
    position: absolute;
    left: 27px;
    top: 478px;
    writing-mode: vertical-rl;
    white-space: nowrap;
    font-family: "Cinzel", serif;
    font-size: 16px;
    letter-spacing: 0.3em;
    color: var(--ink-white);
  }
  .spine-mark {
    position: absolute;
    left: 10px;
    top: 758px;
  }

  /* Front cover */
  .portrait {
    position: absolute;
    left: 552px;
    top: 0;
    width: 648px;
    height: 660px;
    background:
      radial-gradient(ellipse 16% 10% at 57% 50%, var(--skin-warm) 0%, rgba(201,168,156,0) 100%),
      radial-gradient(ellipse 55% 60% at 60% 36%, var(--hair-light) 0%, var(--hair-mid) 45%, rgba(79,91,89,0) 100%);
  }
  .front-author {
    position: absolute;
    left: 700px;
    top: 36px;
    width: 420px;
    text-align: center;
    font-family: "Cinzel", serif;
    font-size: 25px;
    letter-spacing: 0.36em;
    color: var(--ink-dark);
    white-space: nowrap;
  }
  .front-title {
    position: absolute;
    left: 680px;
    top: 440px;
    width: 500px;
    margin: 0;
    text-align: center;
    font-weight: normal;
    text-shadow: 2px 3px 6px rgba(0,0,0,0.35);
  }
  .front-title .script {
    display: block;
    font-family: "Allura", cursive;
    font-size: 92px;
    line-height: 84px;
    white-space: nowrap;
  }
  .front-title .script-small {
    display: block;
    font-family: "Allura", cursive;
    font-size: 50px;
    line-height: 40px;
  }
  .front-title .caps {
    display: block;
    font-family: "Cinzel", serif;
    font-size: 98px;
    line-height: 96px;
  }
  .front-publisher {
    position: absolute;
    left: 680px;
    top: 778px;
    width: 500px;
    text-align: center;
  }
</style>
</head>
<body>
<div class="book-wrap">

  <section class="back-cover">
    <div class="back-title">
      <span class="script">Trois saisons au bord</span>
      <span class="script-small">du vieux</span>
      <span class="caps">Port</span>
    </div>
    <p class="blurb">Lorem ipsum dolor sit amet, consectetur adipiscing elit. Etiam nisi diam, convallis at dictum in, dapibus sit amet mi. Praesent rutrum lacus magna, eget molestie velit lobortis non. Etiam sollicitudin tristique massa at sodales. Duis faucibus egestas odio pretium facilisis. Etiam scelerisque in mauris sed interdum. Nullam diam turpis, sodales ut feugiat in, suscipit in erat. Nullam et risus egestas, porta elit vel, semper lacus. Cras pretium consequat vestibulum. In id sapien ut ex blandit suscipit a sit amet mauris. Ut pharetra gravida tempus. Sed ornare quam sed quam convallis, bibendum pulvinar magna sollicitudin. Duis vel tempor enim. Nulla sit amet urna ac ex pretium ullamcorper.</p>
    <div class="code-box"></div>
    <div class="publisher back-publisher">Editions Basalte</div>
  </section>

  <section class="spine">
    <div class="spine-title">Trois saisons au bord du vieux <span class="caps">PORT</span></div>
    <div class="spine-author">MIREILLE CANTAL</div>
    <svg class="spine-mark" width="52" height="52" viewBox="0 0 52 52" aria-hidden="true">
      <circle cx="26" cy="26" r="26" fill="#ffffff"/>
    </svg>
  </section>

  <section class="front-cover">
    <div class="portrait" role="img" aria-label="Close portrait of a silver-haired woman, windswept hair across her face"></div>
    <div class="front-author">MIREILLE CANTAL</div>
    <h1 class="front-title">
      <span class="script">Trois saisons</span>
      <span class="script">au bord du</span>
      <span class="script-small">vieux</span>
      <span class="caps">PORT</span>
    </h1>
    <div class="publisher front-publisher">Editions Basalte</div>
  </section>

</div>
</body>
</html>
```